Delcourt Realty Business Cards

Design business card

Target Market(s)

High-End Buyer of Real Estate over $1 million dollars

Industry/Entity Type

Realtor

Contact Information for Business Card

Lena Delcourt R(S) LIC.# 41972
Cell 555 246-1938
Email Lena@Delcourt.example
Website IsleFreshHomes.example

Also Need Cards for:

Hank Delcourt R(B) LIC# 69418
C 555 613-7052
E Hank@Delcourt.example
W IsleFreshHomes.example

Colors

Designer to choose colors to be used in the design.

Requirements
Must have
• Address on back:
• 287 Pohaku Cir. , Wailea HI 96753
• Logo on back
Nice to have
• I would like the phone numbers and email address to be big so people can read it easily
Should not have
• Very small print Except For: address (287 Pohaku Cir. Wailea HI 96753)

```html
<!DOCTYPE html>
<html lang="en">
<head>
<meta charset="utf-8">
<title>Delcourt Realty Business Cards</title>
<link href="https://fonts.googleapis.com/css2?family=Montserrat:wght@300;500;600&family=Fira+Sans:wght@400&display=swap" rel="stylesheet">
<style>
  :root {
    --backdrop-centre: #e7e8e9;
    --backdrop-edge: #cfd0d2;
    --card-white: #ffffff;
    --ink: #231f20;
    --accent-blue: #29a9e0;
    --back-centre: #3a3a3b;
    --back-edge: #1f1d1e;
    --text-light: #ffffff;
  }
  html, body {
    margin: 0;
    padding: 0;
    overflow: hidden;
  }
  .canvas {
    position: relative;
    width: 800px;
    height: 1200px;
    box-sizing: border-box;
    border: 1px solid #8f9092;
    background: radial-gradient(circle at 50% 50%, var(--backdrop-centre) 0%, var(--backdrop-edge) 75%);
    overflow: hidden;
  }
  .card {
    position: absolute;
    width: 504px;
    height: 288px;
    overflow: hidden;
  }
  .card-front {
    left: 148px;
    top: 174px;
    background: var(--card-white);
  }
  .agent-name {
    position: absolute;
    left: 21px;
    top: 24px;
    margin: 0;
    font-family: "Montserrat", sans-serif;
    font-weight: 600;
    font-size: 21px;
    line-height: 1;
    color: var(--ink);
  }
  .agent-licence {
    position: absolute;
    left: 21px;
    top: 46px;
    margin: 0;
    font-family: "Montserrat", sans-serif;
    font-weight: 300;
    font-size: 13px;
    line-height: 1;
    color: var(--ink);
  }
  .brand-name {
    position: absolute;
    font-family: "Montserrat", sans-serif;
    font-weight: 600;
    letter-spacing: 2px;
    line-height: 1.1;
    text-transform: uppercase;
  }
  .card-front .brand-name {
    left: 22px;
    top: 100px;
    font-size: 22px;
    color: var(--ink);
  }
  .contact-list {
    position: absolute;
    right: 20px;
    top: 93px;
    margin: 0;
    padding: 0;
    list-style: none;
    font-family: "Fira Sans", sans-serif;
    font-size: 16px;
    color: var(--ink);
    text-align: right;
  }
  .contact-list li {
    display: flex;
    align-items: center;
    justify-content: flex-end;
    gap: 8px;
    height: 36px;
  }
  .contact-icon {
    width: 9px;
    height: 9px;
    fill: var(--ink);
  }
  .front-bands {
    position: absolute;
    left: 0;
    top: 0;
    width: 504px;
    height: 288px;
  }
  .card-back {
    left: 118px;
    top: 704px;
    background: radial-gradient(ellipse at 50% 45%, var(--back-centre) 0%, var(--back-edge) 70%);
  }
  .card-back .brand-name {
    left: 0;
    right: 0;
    top: 113px;
    text-align: center;
    font-size: 26px;
    color: var(--text-light);
  }
  .office-address {
    position: absolute;
    left: 0;
    right: 0;
    top: 232px;
    margin: 0;
    display: flex;
    justify-content: center;
    align-items: center;
    gap: 5px;
    font-family: "Fira Sans", sans-serif;
    font-size: 18px;
    color: var(--text-light);
  }
  .pin-icon {
    width: 11px;
    height: 15px;
    fill: var(--text-light);
  }
</style>
</head>
<body>
<div class="canvas">

  <section class="card card-front" aria-label="Business card front">
    <svg class="front-bands" viewBox="0 0 630 360" aria-hidden="true">
      <polygon points="0,213 152,355 0,355" fill="var(--ink)"/>
      <polygon points="73,280 108,280 135,305 630,305 630,355 152,355" fill="var(--accent-blue)"/>
      <polygon points="260,275 630,275 630,305 287,305" fill="var(--ink)"/>
    </svg>

    <h1 class="agent-name">Lena Delcourt R(S)</h1>
    <p class="agent-licence">LIC.# 41972</p>

    <div class="brand-name">Delcourt<br>Realty</div>

    <ul class="contact-list">
      <li>555 246-1938
        <svg class="contact-icon" viewBox="0 0 10 10" aria-hidden="true"><path d="M2 0.5 L3.8 2.6 L2.9 3.8 Q4 6 6.2 7.1 L7.4 6.2 L9.5 8 L8.2 9.5 Q4.5 9.5 1.8 6.8 Q0.5 4.5 0.5 1.8 Z"/></svg>
      </li>
      <li>Lena@Delcourt.example
        <svg class="contact-icon" viewBox="0 0 10 10" aria-hidden="true"><rect x="0" y="2" width="10" height="6.5"/><polyline points="0.5,2.5 5,6 9.5,2.5" fill="none" stroke="#fff" stroke-width="0.9"/></svg>
      </li>
      <li>IsleFreshHomes.example
        <svg class="contact-icon" viewBox="0 0 10 10" aria-hidden="true"><circle cx="5" cy="5" r="4.6"/><g fill="none" stroke="#fff" stroke-width="0.7"><ellipse cx="5" cy="5" rx="2" ry="4.6"/><line x1="0.4" y1="5" x2="9.6" y2="5"/><line x1="5" y1="0.4" x2="5" y2="9.6"/></g></svg>
      </li>
    </ul>
  </section>

  <section class="card card-back" aria-label="Business card back">
    <div class="brand-name">Delcourt<br>Realty</div>
    <p class="office-address">
      <svg class="pin-icon" viewBox="0 0 11 15" aria-hidden="true"><path d="M5.5 0 A5.5 5.5 0 0 1 11 5.5 C11 9 5.5 15 5.5 15 C5.5 15 0 9 0 5.5 A5.5 5.5 0 0 1 5.5 0 Z M5.5 3.3 A2.2 2.2 0 1 0 5.5 7.7 A2.2 2.2 0 1 0 5.5 3.3 Z" fill-rule="evenodd"/></svg>
      287 Pohaku Cir. , Kahiko Bay HI 96790
    </p>
  </section>

</div>
</body>
</html>
```